Business card and company stationary - Corvane Cleaning Ltd

1. Who are we and who are our customers?

o We are a relatively new cleaning company, established December 2008. We are a small company. We have 24 staff and we offer domestic and commercial cleaning services.
o We both (me and my wife) have been working for many years in the cleaning industry. We worked for some of the biggest and best cleaning companies in UK. We’ve been operatives, supervisors and managers.
o Inevitably after so many years of working for someone else, we decided to start our own business.
o Our domestic customers are middle class families and busy professionals. We’ve got some commercial customers, mainly offices.
o We are growing steadily.

2. What do we do? What are our services?

o Cleaning. We’ve got range of services - not to many but still can be daunting and confusing for some.
o Generally we’ve got domestic and commercial clients. The approach to the domestic cleaning customers is different to the commercial. In the way we want to say that it is cleaning that we do, but we acknowledge the environment and we appreciate the personal circumstances and requirements that are present. We do care, we listen and we try to work out the best possible way to complete our work.
o Mainly we get our work through referrals

3. What do we want with our stationery ?

o To place and maintain our message and reach out to people and organisations
o We want to advertise, communicate and sale.
o We are going to sell services.
o Increase membership, loyalty and support.

We are after business card design, headed letter and compliment slip.
We would like the headed letter to be created in formats suitable for :
- printing format
- also for use in our daily correspondence via e mail with clients and staff in a easy to edit and write format

The website we have is still under contraction and the domain is corvanecleaning.example

Target Market(s)

Families, individuals, businesses.

Industry/Entity Type

Cleaning Service

Contact Information for Business Card

FRONT :
Company Name - Corvane Cleaning Ltd
Company address - 41 Pelbury Rd, Pelbury, Essex, RM14 7QT
Name - Mrs. Teodora Vasilkova - Tedi
Title - Managing Director
Company phone - 020 8837 2591
E mail - tedi.vasilkova@corvanecleaning.example

BACK :

Company website - corvanecleaning.example
E mail - enquiries@corvanecleaning.example

Font styles to use
Serif

Requirements
Must have
• The above items and company logo...maybe at the back. But I'm free for any suggestions.

```html
<!DOCTYPE html>
<html lang="en">
<head>
<meta charset="utf-8">
<title>Corvane Cleaning Ltd – Business Card</title>
<link href="https://fonts.googleapis.com/css2?family=Open+Sans:wght@400;600;700&display=swap" rel="stylesheet">
<style>
  :root {
    --backdrop: #efefef;
    --paper: #ffffff;
    --sky: #33c3f0;
    --ink: #1d1d1d;
  }
  html, body {
    margin: 0;
    padding: 0;
    width: 1200px;
    height: 800px;
    overflow: hidden;
    background: var(--backdrop);
    font-family: "Open Sans", Arial, sans-serif;
  }
  .sheet { position: relative; width: 1200px; height: 800px; }
  .card {
    position: absolute;
    top: 242px;
    width: 550px;
    height: 315px;
    overflow: hidden;
    box-shadow: 0 2px 6px rgba(0,0,0,0.12);
  }
  .card--front { left: 30px; background: var(--paper); }
  .card--back  { left: 620px; background: var(--sky); }

  /* front */
  .brand {
    position: absolute;
    left: 30px;
    top: 28px;
    width: 200px;
    text-align: center;
    color: var(--ink);
  }
  .brand__mark {
    width: 70px;
    height: 70px;
    margin: 0 auto 10px;
    border-radius: 50%;
    background: var(--sky);
  }
  .brand__name {
    font-weight: 400;
    font-size: 27px;
    letter-spacing: 4px;
    line-height: 1;
    text-transform: uppercase;
  }
  .brand__sub {
    font-weight: 400;
    font-size: 10px;
    letter-spacing: 6px;
    margin-top: 6px;
    text-transform: uppercase;
  }
  .accent-bar { position: absolute; background: var(--sky); }
  .accent-bar--left { left: 48px; top: 215px; width: 24px; height: 100px; }
  .accent-bar--top  { left: 276px; top: 0; width: 24px; height: 62px; }

  .person {
    position: absolute;
    left: 86px;
    top: 240px;
    color: var(--ink);
  }
  .person__name { font-weight: 700; font-size: 17px; line-height: 1.1; white-space: nowrap; }
  .person__role { font-weight: 400; font-size: 11px; margin-top: 1px; }

  .contact-icon {
    position: absolute;
    width: 26px;
    height: 26px;
    background: var(--sky);
  }
  .contact-icon svg {
    position: absolute;
    left: 5px;
    top: 5px;
    width: 16px;
    height: 16px;
  }
  .contact-list {
    position: absolute;
    left: 326px;
    top: 76px;
    margin: 0;
    padding: 0;
    list-style: none;
    color: var(--ink);
    font-size: 11.5px;
    font-weight: 400;
  }
  .contact-list li {
    height: 32px;
    line-height: 26px;
    white-space: nowrap;
  }

  /* back */
  .check {
    position: absolute;
    width: 26px;
    height: 26px;
    background: var(--paper);
  }
  .emblem {
    position: absolute;
    left: 0;
    top: 82px;
    width: 550px;
    text-align: center;
    color: var(--ink);
  }
  .emblem__mark {
    width: 96px;
    height: 96px;
    margin: 0 auto 12px;
    border-radius: 50%;
    border: 5px solid var(--ink);
    box-sizing: border-box;
    background: var(--paper);
  }
  .emblem__name {
    font-weight: 600;
    font-size: 20px;
    letter-spacing: 3px;
    text-transform: uppercase;
  }
  .emblem__links {
    margin-top: 10px;
    font-size: 12px;
    line-height: 18px;
    font-weight: 400;
  }
</style>
</head>
<body>
<div class="sheet">

  <section class="card card--front" aria-label="Business card front">
    <div class="brand">
      <div class="brand__mark"></div>
      <div class="brand__name">Corvane</div>
      <div class="brand__sub">Cleaning Ltd</div>
    </div>

    <div class="accent-bar accent-bar--left"></div>
    <div class="person">
      <div class="person__name">Mrs. Teodora Vasilkova - Tedi</div>
      <div class="person__role">Managing Director</div>
    </div>

    <div class="accent-bar accent-bar--top"></div>

    <div class="contact-icon" style="left:276px; top:76px;">
      <svg viewBox="0 0 16 16"><rect width="16" height="16" fill="#1d1d1d"/><path d="M8 3a3 3 0 0 0-3 3c0 2.3 3 6 3 6s3-3.7 3-6a3 3 0 0 0-3-3zm0 4.2A1.2 1.2 0 1 1 8 4.8a1.2 1.2 0 0 1 0 2.4z" fill="#fff"/></svg>
    </div>
    <div class="contact-icon" style="left:294px; top:108px;">
      <svg viewBox="0 0 16 16"><rect width="16" height="16" fill="#1d1d1d"/><path d="M5 3.5l1.6 2.4-1 1c.6 1.3 1.6 2.3 2.9 2.9l1-1 2.4 1.6-.8 1.8c-3.6-.2-6.6-3.2-6.8-6.8z" fill="#fff"/></svg>
    </div>
    <div class="contact-icon" style="left:258px; top:140px;">
      <svg viewBox="0 0 16 16"><rect width="16" height="16" fill="#1d1d1d"/><rect x="5" y="3" width="6" height="10" rx="1" fill="none" stroke="#fff" stroke-width="1.2"/><circle cx="8" cy="11.2" r="0.7" fill="#fff"/></svg>
    </div>
    <div class="contact-icon" style="left:284px; top:172px;">
      <svg viewBox="0 0 16 16"><rect width="16" height="16" fill="#1d1d1d"/><rect x="3.5" y="5" width="9" height="6.5" fill="none" stroke="#fff" stroke-width="1.1"/><path d="M3.5 5l4.5 3.5L12.5 5" fill="none" stroke="#fff" stroke-width="1.1"/></svg>
    </div>
    <div class="contact-icon" style="left:248px; top:204px;">
      <svg viewBox="0 0 16 16"><rect width="16" height="16" fill="#1d1d1d"/><circle cx="8" cy="8" r="4.5" fill="none" stroke="#fff" stroke-width="1.1"/><path d="M3.5 8h9M8 3.5c-2 2.5-2 6.5 0 9M8 3.5c2 2.5 2 6.5 0 9" fill="none" stroke="#fff" stroke-width="0.9"/></svg>
    </div>

    <ul class="contact-list">
      <li>41 Pelbury Rd, Pelbury, Essex, RM14 7QT</li>
      <li>020 8837 2591</li>
      <li>07700 900 418</li>
      <li>tedi.vasilkova@corvanecleaning.example</li>
      <li>www.corvanecleaning.example</li>
    </ul>
  </section>

  <section class="card card--back" aria-label="Business card back">
    <div class="check" style="left:0; top:0;"></div>
    <div class="check" style="left:26px; top:26px;"></div>
    <div class="check" style="left:0; top:52px;"></div>
    <div class="check" style="left:26px; top:78px;"></div>
    <div class="check" style="left:0; top:104px;"></div>

    <div class="check" style="right:0; bottom:0;"></div>
    <div class="check" style="right:26px; bottom:26px;"></div>
    <div class="check" style="right:0; bottom:52px;"></div>
    <div class="check" style="right:26px; bottom:78px;"></div>
    <div class="check" style="right:0; bottom:104px;"></div>

    <div class="emblem">
      <div class="emblem__mark"></div>
      <div class="emblem__name">Corvane Cleaning Ltd</div>
      <div class="emblem__links">
        <div>corvanecleaning.example</div>
        <div>enquiries@corvanecleaning.example</div>
      </div>
    </div>
  </section>

</div>
</body>
</html>
```